Northway Trade Partners Needs a FRESH website

We would like a creative minded designer to take on the task to Re-design our website. Its a simple 5-7 pages. With no cart, no complex html. Just plain information about our company and products we import and export. Pictures added to the product section. Since Our logo its Blue, we would like the designer to use complementing colors in order to make the website look cleaner and modern.

Target Market(s)

The target audience will be companies looking to purchase plastic related products. Companies looking to purchase large quantities of plastic containers (Shampoo bottles, caps, sprayers, mist sprayers, cosmetic containers etc).

Industry/Entity Type

It Company

Font styles to use
Sans Serif

Requirements
Must have
• We have a section in which we would like to add pictures of some of the products we carry, therefore having an easy and clean way to navigate through the pictures will be a plus.

```html
<!DOCTYPE html>
<html lang="en">
<head>
<meta charset="utf-8">
<title>Northway Trade Partners</title>
<link href="https://fonts.googleapis.com/css2?family=Open+Sans:wght@400;600;700&display=swap" rel="stylesheet">
<style>
:root{
  --blue:#1e88d0;
  --blue-dark:#1670b0;
  --ink:#333;
  --muted:#777;
  --line:#e2e2e2;
  --band:#e9e9e9;
  --footer-bar:#3a3a3a;
  --white:#fff;
}
*{box-sizing:border-box;margin:0;padding:0}
html,body{width:804px;height:1200px;overflow:hidden}
body{font-family:"Open Sans",Arial,sans-serif;color:var(--ink);background:var(--white);position:relative}
.abs{position:absolute}
.site-header{left:0;top:0;width:804px;height:60px;background:var(--white)}
.brand{left:82px;top:0;width:118px;height:82px;background:var(--blue);z-index:3;display:flex;flex-direction:column;align-items:center;justify-content:center;gap:6px}
.brand-dot{width:22px;height:22px;border-radius:50%;background:var(--white)}
.brand-name{color:var(--white);font-size:10.5px;font-weight:600;text-align:center;line-height:1.2}
.main-nav{right:70px;top:22px;display:flex;gap:30px;font-size:11.5px;font-weight:600;text-transform:uppercase;color:#555}
.main-nav a{color:inherit;text-decoration:none;position:relative}
.main-nav a.active{color:var(--blue)}
.main-nav a.active::after{content:"";position:absolute;left:0;right:0;bottom:-6px;height:2px;background:var(--blue)}
.hero{left:0;top:60px;width:804px;height:355px;background:linear-gradient(160deg,#8e8a78 0%,#d9d0a2 35%,#f1e9c2 55%,#b7ae90 80%,#6f6a5c 100%)}
.hero-caption{right:0;top:330px;width:540px;height:52px;background:rgba(30,30,30,.7);color:var(--white);font-size:19px;font-weight:600;letter-spacing:.5px;display:flex;align-items:center;justify-content:flex-end;padding-right:60px;z-index:2}
.section-title{color:var(--blue);font-size:19px;font-weight:400}
.welcome-title{left:54px;top:445px}
.welcome-photo{left:54px;top:485px;width:160px;height:168px;background:linear-gradient(135deg,#c0402a,#8d2a20 60%,#5a1d18)}
.welcome-text{left:236px;top:485px;width:240px;font-size:8.6px;line-height:1.55;color:var(--muted)}
.welcome-text p+p{margin-top:12px}
.news-title{left:520px;top:445px}
.news-list{left:520px;top:487px;width:232px}
.news-item{display:flex;gap:10px;margin-bottom:12px;padding-bottom:12px;border-bottom:1px solid var(--line)}
.news-item:last-child{border:0}
.news-thumb{width:78px;height:40px;flex:none}
.news-head{font-size:8.5px;color:var(--blue);font-weight:600}
.news-desc{font-size:8px;line-height:1.4;color:var(--muted);margin-top:2px}
.products-title{left:0;top:700px;width:804px;text-align:center;font-size:21px}
.products-band{left:0;top:752px;width:804px;height:252px;background:var(--band)}
.product-grid{left:54px;top:785px;width:700px;display:grid;grid-template-columns:repeat(3,1fr);row-gap:50px;column-gap:20px}
.product{display:flex;gap:12px}
.product-icon{width:42px;height:42px;border-radius:50%;background:var(--blue);flex:none;display:flex;align-items:center;justify-content:center}
.product-name{color:var(--blue);font-size:15px;font-weight:400;text-transform:uppercase}
.product-desc{font-size:8.6px;line-height:1.45;color:var(--muted);margin-top:2px}
.footer-col{top:1030px}
.footer-col h3{font-size:12.5px;font-weight:600;color:var(--ink);padding-bottom:8px;border-bottom:1px solid var(--line);width:150px;margin-bottom:10px}
.footer-col ul{list-style:none;font-size:8.6px;color:var(--muted);line-height:2.1}
.footer-col li::before{content:"•";margin-right:6px;color:#999}
.contact-list li::before{content:none}
.contact-list li{display:flex;gap:10px;align-items:center}
.follow-text{font-size:8.6px;color:var(--muted);line-height:1.4;width:150px}
.socials{display:flex;gap:8px;margin-top:10px}
.social{width:24px;height:24px;border-radius:50%;background:var(--blue)}
.copyright{left:0;top:1168px;width:804px;height:32px;background:var(--footer-bar);color:#ccc;font-size:8.6px;padding:10px 54px}
</style>
</head>
<body>

<header class="site-header abs"></header>
<div class="brand abs"><span class="brand-dot"></span><span class="brand-name">Northway Trade Partners</span></div>
<nav class="main-nav abs">
  <a class="active" href="#">Home</a><a href="#">About us</a><a href="#">Products</a><a href="#">Mission</a><a href="#">Contact</a>
</nav>

<div class="hero abs" role="img" aria-label="Close-up of white and yellow plastic resin pellets"></div>
<div class="hero-caption abs">DUIS AUTEM VEL EUM IRIURE DOLORIN</div>

<h2 class="section-title welcome-title abs">Welcome to Our Website</h2>
<div class="welcome-photo abs" role="img" aria-label="Pile of red and orange plastic pellets"></div>
<div class="welcome-text abs">
  <p>Eu lorem nostrud tempor velit, sed do magna aliqua quis erat volutpat. Ut enim ad minim veniam, quis nostrud exercitation ullamco laboris nisi ut aliquip ex ea commodo consequat duis aute irure dolor in reprehenderit.</p>
  <p>Eu lorem nostrud tempor velit, sed do magna aliqua quis erat volutpat. Ut enim ad minim veniam, quis nostrud exercitation ullamco laboris nisi ut aliquip ex ea commodo consequat duis aute irure dolor in reprehenderit.</p>
</div>

<h2 class="section-title news-title abs">Latest News</h2>
<div class="news-list abs">
  <div class="news-item">
    <div class="news-thumb" role="img" aria-label="Blue plastic pellets" style="background:linear-gradient(135deg,#2b7fc4,#9cc8ec)"></div>
    <div><div class="news-head">Duis autem vel eum iriure dolor</div><div class="news-desc">Bravo cause the enduring sun fueled by fitness and care.</div></div>
  </div>
  <div class="news-item">
    <div class="news-thumb" role="img" aria-label="Multicoloured plastic granules" style="background:linear-gradient(135deg,#d84a3a,#e8c04a 50%,#5aa04a)"></div>
    <div><div class="news-head">Duis autem vel eum iriure dolor</div><div class="news-desc">Bravo cause the enduring sun fueled by fitness and care.</div></div>
  </div>
  <div class="news-item">
    <div class="news-thumb" role="img" aria-label="Orange and blue plastic pellets" style="background:linear-gradient(135deg,#e07a2a,#4a8ed0)"></div>
    <div><div class="news-head">Duis autem vel eum iriure dolor</div><div class="news-desc">Bravo cause the enduring sun fueled by fitness and care.</div></div>
  </div>
</div>

<h2 class="section-title products-title abs">Products</h2>
<div class="products-band abs"></div>
<div class="product-grid abs">
  <div class="product">
    <div class="product-icon"><svg width="18" height="20" viewBox="0 0 18 20"><path d="M9 1 C9 1 2 10 2 13 a7 7 0 0 0 14 0 C16 10 9 1 9 1Z" fill="#fff"/></svg></div>
    <div><div class="product-name">PET</div><div class="product-desc">Dolor sit vivamus faucibus, mi quis convallis tempus, augue et.</div></div>
  </div>
  <div class="product">
    <div class="product-icon"><svg width="20" height="18" viewBox="0 0 20 18"><path d="M10 1 L19 17 H1Z" fill="none" stroke="#fff" stroke-width="2"/></svg></div>
    <div><div class="product-name">PET RESIN</div><div class="product-desc">Dolor sit vivamus faucibus, mi quis convallis tempus, augue et.</div></div>
  </div>
  <div class="product">
    <div class="product-icon"><svg width="20" height="20" viewBox="0 0 20 20"><rect x="6" y="2" width="8" height="16" rx="3" transform="rotate(40 10 10)" fill="#fff"/></svg></div>
    <div><div class="product-name">PET CONTAINERS</div><div class="product-desc">Dolor sit vivamus faucibus, mi quis convallis tempus, augue et.</div></div>
  </div>
  <div class="product">
    <div class="product-icon"><svg width="14" height="22" viewBox="0 0 14 22"><rect x="5" y="1" width="4" height="4" fill="#fff"/><rect x="2" y="6" width="10" height="15" rx="3" fill="#fff"/></svg></div>
    <div><div class="product-name">P.E.P.P. Containers</div><div class="product-desc">Dolor sit vivamus faucibus, mi quis convallis tempus, augue et.</div></div>
  </div>
  <div class="product">
    <div class="product-icon"><svg width="16" height="22" viewBox="0 0 16 22"><rect x="3" y="1" width="9" height="4" fill="#fff"/><rect x="6" y="5" width="3" height="4" fill="#fff"/><rect x="3" y="9" width="10" height="12" rx="2" fill="#fff"/></svg></div>
    <div><div class="product-name">SPRAYERS</div><div class="product-desc">Dolor sit vivamus faucibus, mi quis convallis tempus, augue et.</div></div>
  </div>
  <div class="product">
    <div class="product-icon"><svg width="20" height="20" viewBox="0 0 20 20"><circle cx="10" cy="10" r="7" fill="none" stroke="#fff" stroke-width="2"/><circle cx="10" cy="10" r="3" fill="#fff"/></svg></div>
    <div><div class="product-name">MOLDS</div><div class="product-desc">Dolor sit vivamus faucibus, mi quis convallis tempus, augue et.</div></div>
  </div>
</div>

<section class="footer-col abs" style="left:54px">
  <h3>Site Map</h3>
  <ul><li>Home</li><li>About</li><li>Programs</li><li>Contact Us</li></ul>
</section>
<section class="footer-col abs" style="left:190px">
  <h3>Links</h3>
  <ul><li>Consectetuer</li><li>Praesent luptum</li><li>Duis autem vaum</li><li>Nam liber tempor</li></ul>
</section>
<section class="footer-col abs" style="left:352px">
  <h3>Contact</h3>
  <ul class="contact-list">
    <li><svg width="9" height="12" viewBox="0 0 9 12"><path d="M4.5 0a4.5 4.5 0 0 0-4.5 4.5C0 8 4.5 12 4.5 12S9 8 9 4.5A4.5 4.5 0 0 0 4.5 0Z" fill="#555"/><circle cx="4.5" cy="4.5" r="1.6" fill="#fff"/></svg><span># 22, Harbor Lane<br>58 Lakeside Row, NA 4100</span></li>
    <li><svg width="11" height="8" viewBox="0 0 11 8"><rect width="11" height="8" fill="#555"/><path d="M0 0 L5.5 4.5 L11 0" fill="none" stroke="#fff"/></svg><span>info@northwaytrade.com</span></li>
    <li><svg width="10" height="10" viewBox="0 0 10 10"><path d="M2 0 L4 3 L3 4 Q4 6 6 7 L7 6 L10 8 L8 10 Q1 9 0 2Z" fill="#555"/></svg><span>01 2345 6789</span></li>
  </ul>
</section>
<section class="footer-col abs" style="left:542px">
  <h3>Follow Us</h3>
  <p class="follow-text">Follow our news and events through social networks</p>
  <div class="socials"><span class="social"></span><span class="social"></span><span class="social"></span></div>
</section>

<footer class="copyright abs">Copyright © 2015. All Rights Reserved</footer>

</body>
</html>
```